Vellmar Detailing – Premium Automotive Detailing Studio Website Design

We're launching a premium automotive detailing studio called Vellmar Detailing, and we’re looking for a clean, minimal, and high-end website design (desktop + mobile version). The studio targets owners of luxury vehicles who care deeply about aesthetics, perfection, and exceptional service.
This project is about more than just showing services , it should feel like a luxury experience from the very first second. The design should be modern, minimalistic, elegant, and clearly aimed at an upscale market.
We’re looking for a designer who can translate our physical studio’s premium interior and architectural feel into a digital presence.
What we want the website to feel like:
Clean and modern
Professional and luxurious
Minimal and not cluttered
Light animations or transitions to add polish
Stylish and cinematic
Design freedom:
We trust your design direction. We are not providing strict color codes or layout instructions, we want you to create what you believe works best based on our brand positioning and target audience. Just keep it premium, modern, and well-organized.
What the website should include:
Hero section with a bold visual (image or video)
About the Studio — a few blocks explaining our story and focus on quality
Service Overview — clearly showing what we offer (detailing, ceramic coating, interior, etc.)
Gallery/Showcase — show off our work with cars, interior, and the space itself
Client Lounge Area — mention comfort, coffee, and waiting space
Testimonials — social proof from satisfied clients
Location & contact section — map, address, contact form
Footer, simple with nav, contact info, and optional social media
Target audience:
Owners of high-end vehicles (Torvani, Kellard, etc.)
Car collectors and detailing enthusiasts
People looking for premium-level service and presentation
Brands/creators booking our photo studio

```html
<!DOCTYPE html>
<html lang="en">
<head>
<meta charset="utf-8">
<title>Vellmar Detailing – Premium Car Detailing Studio</title>
<link href="https://fonts.googleapis.com/css2?family=Krona+One&family=Poppins:ital,wght@0,400;0,500;0,600;0,700;1,500&display=swap" rel="stylesheet">
<style>
:root{
  --red:#d3001b;
  --red-btn:#d6102b;
  --black:#000;
  --ink:#111;
  --white:#fff;
  --grey:#555;
  --head:"Krona One", sans-serif;
  --body:"Poppins", sans-serif;
}
*{margin:0;padding:0;box-sizing:border-box}
html,body{width:1200px;height:5396px;overflow:hidden}
body{position:relative;font-family:var(--body);color:var(--ink);background:var(--white)}
.abs{position:absolute}
.btn{position:absolute;display:flex;align-items:center;justify-content:center;background:var(--red-btn);color:var(--white);font:700 14px var(--body);text-transform:uppercase;border-radius:30px;letter-spacing:.3px}
.h-xl{font-family:var(--head);text-transform:uppercase;letter-spacing:1px;line-height:1.1}
.eyebrow{font:600 21px var(--body);text-transform:uppercase;letter-spacing:.5px}

/* hero */
.hero{left:0;top:0;width:1200px;height:796px;background:radial-gradient(ellipse at 55% 45%,#5a0c12 0%,#2a1416 30%,#0d0d0f 60%) ,#000}
.hero-fade{left:0;top:560px;width:1200px;height:240px;background:linear-gradient(to bottom,rgba(255,255,255,0),#fff 90%)}
.hero-car{left:170px;top:240px;width:890px;height:310px;border-radius:140px 160px 40px 40px;background:linear-gradient(100deg,#6b0a12,#c8101f 45%,#8a8d92 85%,#d8d8d8);opacity:.85}
.topbar{left:128px;top:24px;color:#fff;font:600 15px var(--body)}
.nav{left:128px;top:70px;width:946px;display:flex;justify-content:space-between;color:#fff;font:600 13.5px var(--body);text-transform:uppercase}
.nav .active{border-bottom:2px solid #fff;padding-bottom:8px}
.nav .gap{width:120px}
.brand{left:530px;top:24px;width:140px;text-align:center;color:#fff;font:600 15px var(--body);line-height:1.25;letter-spacing:2px;text-transform:uppercase}
.hero-title{left:128px;top:205px;color:#fff;font-size:28px}

/* about */
.about-title{left:127px;top:790px;font-size:40px;color:#000}
.about-text{left:126px;top:906px;width:500px;font:400 15px/1.9 var(--body);color:#222}

/* services */
.services{left:0;top:1204px;width:1200px;height:780px;background:var(--black)}
.services .eyebrow{color:#fff;position:absolute;top:92px;width:100%;text-align:center}
.services .h-xl{position:absolute;top:128px;width:100%;text-align:center;color:#fff;font-size:40px}
.card{position:absolute;top:212px;width:300px;height:392px;background:#fff}
.card .pic{height:168px}
.card h3{margin-top:26px;text-align:center;font:600 21px var(--body);text-transform:uppercase}
.card p{margin:14px 28px 0;text-align:center;font:400 14px/1.4 var(--body);color:#333}
.card .more{position:absolute;bottom:22px;width:100%;text-align:center;font:700 13.5px var(--body);text-transform:uppercase}
.btn-outline{left:496px;top:650px;width:206px;height:48px;border:2px solid #fff;font-size:13.5px}

/* gallery */
.gallery-eyebrow{top:2064px;width:1200px;text-align:center;color:#444}
.gallery-title{top:2096px;width:1200px;text-align:center;font-size:40px;color:#000}
.shot{top:2202px;height:358px;border-radius:12px}
.dots{left:540px;top:2620px;display:flex;gap:8px}
.dots span{width:9px;height:9px;border-radius:50%;background:#ccc}
.dots span:first-child{background:#888}

/* lounge */
.lounge{left:0;top:2740px;width:1200px;height:580px;background:linear-gradient(180deg,#26262b 0%,#3a1a20 45%,#5e0f18 100%)}
.lounge h2{position:absolute;top:70px;width:100%;text-align:center;color:#fff;font-size:40px}
.lounge h2 span{color:var(--red-btn)}
.perk{position:absolute;top:180px;width:296px;height:285px;border:2px solid rgba(255,255,255,.45);text-align:center;color:#fff}
.perk svg{margin-top:34px}
.perk h3{margin-top:22px;font:600 21px var(--body);text-transform:uppercase}
.perk p{margin:14px 30px 0;font:400 14.5px/1.45 var(--body);color:#ddd}

/* testimonials */
.testimonials{left:0;top:3320px;width:1200px;height:568px;background:var(--red)}
.testimonials .eyebrow{position:absolute;top:95px;width:100%;text-align:center;color:#fff}
.testimonials .h-xl{position:absolute;top:133px;width:100%;text-align:center;color:#fff;font-size:40px}
.quote{position:absolute;top:290px;width:420px;color:#fff}
.quote .avatar{position:absolute;left:0;top:2px;width:56px;height:56px;border-radius:50%;border:2px solid #fff}
.quote p{margin-left:70px;font:500 italic 14.5px/1.9 var(--body)}
.quote .who{margin:12px 0 0 70px;font:700 13px var(--body);text-transform:uppercase}
.quote .mark{position:absolute;right:-20px;top:100px;font:700 64px/1 var(--head)}

/* contact */
.contact-eyebrow{left:127px;top:4050px;color:#000;font-weight:700}
.contact-title{left:126px;top:4088px;font-size:40px;color:#000}
.contact-text{left:126px;top:4160px;width:390px;font:400 14.5px/1.35 var(--body);color:#222}
.info{position:absolute;left:126px;display:flex;align-items:center;gap:22px;font:400 15px/1.35 var(--body);color:#222}
.ico{width:34px;height:34px;border-radius:50%;background:var(--red-btn);display:flex;align-items:center;justify-content:center;flex:none}
.map{left:572px;top:4104px;width:492px;height:346px;background:linear-gradient(135deg,#efe9de,#e3e8ee 50%,#f1e6d2)}

/* form */
.band{left:0;top:4797px;width:1200px;height:599px;background:var(--black)}
.form{left:197px;top:4548px;width:806px;height:409px;background:var(--red-btn)}
.form h2{position:absolute;top:54px;width:100%;text-align:center;color:#fff;font-size:32px}
.field{position:absolute;background:#fff;border-radius:3px;font:400 14.5px var(--body);color:#333;padding:10px 12px}
.submit{left:312px;top:318px;width:180px;height:48px;background:#111;font-size:16px}

/* footer */
.foot-brand{left:128px;top:5085px;width:180px;color:#fff;font:600 26px/1.2 var(--body);text-transform:uppercase;letter-spacing:2px}
.divider{top:5020px;width:1px;height:220px;background:#444}
.foot-h{top:5040px;color:#fff;font-size:20px}
.foot-list{font:400 14.5px/1.35 var(--body);color:#bbb}
.foot-contact .row{display:flex;gap:22px;align-items:center;margin-bottom:22px}
.foot-links a{display:block;color:#bbb;text-decoration:none;margin-bottom:12px}
.copy{top:5320px;width:1200px;text-align:center;color:#fff;font:400 14.5px var(--body)}
</style>
</head>
<body>

<!-- hero -->
<section class="abs hero" role="img" aria-label="Detailer pressure-washing a red sports car covered in foam in a dark studio"></section>
<div class="abs hero-car" role="img" aria-label="Red sports car being washed"></div>
<div class="abs hero-fade"></div>
<div class="abs topbar">CALL: 8120 447213</div>
<div class="abs brand">Vellmar<br>Detailing</div>
<a class="btn" style="left:944px;top:15px;width:130px;height:40px">Book a slot</a>
<nav class="abs nav">
  <span class="active">Home</span><span>About us</span><span>Services offer</span><span class="gap"></span><span>Gallery</span><span>Testimonials</span><span>Contact</span>
</nav>
<h1 class="abs h-xl hero-title">Premium car<br>detailing studio</h1>
<a class="btn" style="left:126px;top:296px;width:148px;height:42px">Book a slot</a>
<a class="btn" style="left:838px;top:219px;width:234px;height:54px;font-size:17px">Call:VEL-470-215</a>

<!-- about -->
<h2 class="abs h-xl about-title">About<br>the studio</h2>
<p class="abs about-text">Lorem ipsum dolor sit amet, consectetur adipiscing elit, sed do eiusmod tempor incididunt ut labore et dolore magna aliqua. Quis ipsum suspendisse ultrices gravida. Risus commodo viv erra maecenas accumsan lacus vel facilisis.</p>
<a class="btn" style="left:126px;top:1036px;width:148px;height:44px">Read more</a>

<!-- services -->
<section class="abs services">
  <div class="eyebrow">Service overview</div>
  <h2 class="h-xl">What we offer</h2>
  <article class="card" style="left:126px">
    <div class="pic" role="img" aria-label="Hand polishing a dark car's paintwork" style="background:linear-gradient(135deg,#2a2a2a,#6b6b6b 50%,#b15b3a)"></div>
    <h3>Detailing</h3>
    <p>Lorem ipsum dolor sit amecons ecletur adipiscing elit, sed do eiu smod tempor incididunt ut lab ore et dolore magna alua.</p>
    <div class="more">Read more</div>
  </article>
  <article class="card" style="left:450px">
    <div class="pic" role="img" aria-label="Red car receiving ceramic coating in a misty studio" style="background:linear-gradient(135deg,#1d1d1f,#a3101b 45%,#4a4a4e)"></div>
    <h3>Ceramic coating</h3>
    <p>Lorem ipsum dolor sit amecons ecletur adipiscing elit, sed do eiu smod tempor incididunt ut lab ore et dolore magna alua.</p>
    <div class="more">Read more</div>
  </article>
  <article class="card" style="left:773px">
    <div class="pic" role="img" aria-label="Cleaning a car interior dashboard" style="background:linear-gradient(135deg,#0e1a26,#2d4c66 55%,#7a8a98)"></div>
    <h3>Interior</h3>
    <p>Lorem ipsum dolor sit amecons ecletur adipiscing elit, sed do eiu smod tempor incididunt ut lab ore et dolore magna alua.</p>
    <div class="more">Read more</div>
  </article>
  <a class="btn btn-outline">View all services</a>
</section>

<!-- gallery -->
<div class="abs eyebrow gallery-eyebrow">Gallery/Showcase</div>
<h2 class="abs h-xl gallery-title">Our&nbsp; works</h2>
<div class="abs shot" style="left:29px;width:384px;background:linear-gradient(135deg,#15171a,#4d5257 55%,#b7a878)" role="img" aria-label="Machine polisher on a black car bonnet"></div>
<div class="abs shot" style="left:436px;width:383px;background:linear-gradient(160deg,#2a2e33,#8d949b 50%,#1b1d20)" role="img" aria-label="Foam-covered black car front"></div>
<div class="abs shot" style="left:842px;width:380px;background:linear-gradient(135deg,#6b4a2a,#c48b3a 45%,#1a1a1a)" role="img" aria-label="Polishing pad on a dark car panel"></div>
<div class="abs dots"><span></span><span></span><span></span><span></span><span></span><span></span><span></span><span></span></div>

<!-- lounge -->
<section class="abs lounge" role="img" aria-label="Blurred view of the client lounge">
  <h2 class="h-xl">Client <span>lounge area</span></h2>
  <div class="perk" style="left:126px">
    <svg width="90" height="90" viewBox="0 0 90 90" fill="none" stroke="#fff" stroke-width="2.5"><path d="M20 80 L60 30"/><path d="M30 65 C20 40 45 15 75 10 C75 40 55 65 30 65Z"/></svg>
    <h3>Comfort</h3><p>Lorem ipsum dolor sit amet consectetur adipiscing.</p>
  </div>
  <div class="perk" style="left:450px">
    <svg width="90" height="90" viewBox="0 0 90 90" fill="none" stroke="#fff" stroke-width="2.5"><path d="M15 45 H65 V55 C65 70 55 78 40 78 C25 78 15 70 15 55Z"/><path d="M65 50 C80 50 80 65 63 65"/><path d="M30 35 C25 28 35 22 30 12 M40 35 C35 28 45 22 40 12 M50 35 C45 28 55 22 50 12"/><path d="M10 82 H72"/></svg>
    <h3>Coffee</h3><p>Lorem ipsum dolor sit amet consectetur adipiscing.</p>
  </div>
  <div class="perk" style="left:777px">
    <svg width="90" height="90" viewBox="0 0 90 90" fill="none" stroke="#fff" stroke-width="2.5"><rect x="22" y="10" width="46" height="40" rx="6"/><rect x="10" y="40" width="14" height="32" rx="4"/><rect x="66" y="40" width="14" height="32" rx="4"/><path d="M24 55 H66 V72 H24 M18 72 V82 M72 72 V82"/></svg>
    <h3>Waiting space</h3><p>Lorem ipsum dolor sit amet consectetur adipiscing.</p>
  </div>
</section>

<!-- testimonials -->
<section class="abs testimonials">
  <div class="eyebrow">Testimonials</div>
  <h2 class="h-xl">Satisfied clients</h2>
  <div class="quote" style="left:130px">
    <div class="avatar" role="img" aria-label="Client portrait" style="background:#8a7a70"></div>
    <p>Lorem ipsum dolor sit amet, conctetur adipi scing elit, sed do eiusmod tmpor incididunt ut labore et dolore magna aliquauis ipsumsusp endisse ultrices gravida.us commvram.</p>
    <div class="who">~Jonah Smithe</div>
    <div class="mark">”</div>
  </div>
  <div class="quote" style="left:654px">
    <div class="avatar" role="img" aria-label="Client portrait" style="background:#6f6258"></div>
    <p>Lorem ipsum dolor sit amet, conctetur adipi scing elit, sed do eiusmod tmpor incididunt ut labore et dolore magna aliquauis ipsumsusp endisse ultrices gravida.us commvram.</p>
    <div class="who">~Jonah Smithe</div>
    <div class="mark">”</div>
  </div>
</section>

<!-- contact -->
<div class="abs eyebrow contact-eyebrow">Contact us</div>
<h2 class="abs h-xl contact-title">Let's talk</h2>
<p class="abs contact-text">Lorem ipsum dolor sit amecons ectetur adipiscing elit, sed do eiusmod tempor incididunt ut lab ore et dolore magna aluagravida. Risus commodo viverra maece nas accumsan lacus vel facilisis.</p>
<div class="info" style="top:4280px"><span class="ico"><svg width="16" height="16" viewBox="0 0 24 24" fill="none" stroke="#fff" stroke-width="2.4"><path d="M12 22s7-7 7-12a7 7 0 0 0-14 0c0 5 7 12 7 12z"/><circle cx="12" cy="10" r="2.5"/></svg></span><span>1825 Placeholder,<br>Alderwick, KY, 40118</span></div>
<div class="info" style="top:4334px"><span class="ico"><svg width="16" height="16" viewBox="0 0 24 24" fill="none" stroke="#fff" stroke-width="2.4"><path d="M22 16.9v3a2 2 0 0 1-2.2 2A19.8 19.8 0 0 1 2.1 4.2 2 2 0 0 1 4.1 2h3a2 2 0 0 1 2 1.7l.5 3a2 2 0 0 1-.6 1.8L7.7 9.8a16 16 0 0 0 6.5 6.5l1.3-1.3a2 2 0 0 1 1.8-.6l3 .5a2 2 0 0 1 1.7 2z"/></svg></span><span>info@company.com</span></div>
<div class="info" style="top:4383px"><span class="ico"><svg width="16" height="16" viewBox="0 0 24 24" fill="none" stroke="#fff" stroke-width="2.4"><rect x="3" y="5" width="18" height="14" rx="2"/><path d="M3 7l9 6 9-6"/></svg></span><span>230-555-0148</span></div>
<div class="abs map" role="img" aria-label="Street map showing the studio location"></div>

<!-- form -->
<div class="abs band"></div>
<form class="abs form">
  <h2 class="h-xl">Get in touch</h2>
  <div class="field" style="left:63px;top:111px;width:304px;height:44px">Name:</div>
  <div class="field" style="left:63px;top:172px;width:304px;height:46px">Email:</div>
  <div class="field" style="left:63px;top:237px;width:304px;height:44px">Phone:</div>
  <div class="field" style="left:381px;top:111px;width:360px;height:170px">Message:</div>
  <a class="btn submit">Submit now</a>
</form>

<!-- footer -->
<div class="abs foot-brand">Vellmar<br>Detailing</div>
<div class="abs divider" style="left:381px"></div>
<div class="abs divider" style="left:798px"></div>
<h4 class="abs h-xl foot-h" style="left:471px">Contact</h4>
<div class="abs foot-list foot-contact" style="left:471px;top:5095px">
  <div class="row"><span class="ico"><svg width="16" height="16" viewBox="0 0 24 24" fill="none" stroke="#fff" stroke-width="2.4"><path d="M12 22s7-7 7-12a7 7 0 0 0-14 0c0 5 7 12 7 12z"/><circle cx="12" cy="10" r="2.5"/></svg></span><span>1825 Placeholder Text,<br>Alderwick, KY, 40118</span></div>
  <div class="row"><span class="ico"><svg width="16" height="16" viewBox="0 0 24 24" fill="none" stroke="#fff" stroke-width="2.4"><rect x="3" y="5" width="18" height="14" rx="2"/><path d="M3 7l9 6 9-6"/></svg></span><span>info@company.com</span></div>
  <div class="row"><span class="ico"><svg width="16" height="16" viewBox="0 0 24 24" fill="none" stroke="#fff" stroke-width="2.4"><path d="M22 16.9v3a2 2 0 0 1-2.2 2A19.8 19.8 0 0 1 2.1 4.2 2 2 0 0 1 4.1 2h3a2 2 0 0 1 2 1.7l.5 3a2 2 0 0 1-.6 1.8L7.7 9.8a16 16 0 0 0 6.5 6.5l1.3-1.3a2 2 0 0 1 1.8-.6l3 .5a2 2 0 0 1 1.7 2z"/></svg></span><span>000-555-0172<br>293 5550 1874</span></div>
</div>
<h4 class="abs h-xl foot-h" style="left:886px">Links</h4>
<nav class="abs foot-list foot-links" style="left:886px;top:5096px">
  <a>About the Studio</a><a>Service Overview</a><a>Gallery/Showcase</a><a>Client Lounge Area</a><a>Testimonials</a><a>Location &amp; contact</a>
</nav>
<div class="abs copy">© 2025 Vellmar Detailing&nbsp; All rights reserved.</div>

</body>
</html>
```